Pacific Screen Trade Alliance is preparing a regular newsletter and needs a design

Our association is made up of media companies, TV stations and video on demand companies. As an association our role is to bring industry together to engage in government dialogues, fight video piracy and hold conferences and events. We are starting a regular newsletter to let our members know what activities we have been undertaking on their behalf and what upcoming activities there are. It will be a combination of text and pictures/ graphics. We have made a lot of changes to the association so we need a design which is professional looking, but also creative and future looking. It should also have a sense of entertainment given it is the video entertainment industry we represent. Attached is an example of a recent newsletter but would like to see something a little more dynamic and professional.

Target Market(s)

Executives in media companies

Font styles to use
Serif

Colors

Designer to choose colors to be used in the design.

Requirements
Must have
• A combination of text, photos and graphics in a modern, personable yet professional layout and design

```html
<!DOCTYPE html>
<html lang="en">
<head>
<meta charset="utf-8">
<title>Policy and Piracy Newsletter – Spring 2019</title>
<link rel="stylesheet" href="https://fonts.googleapis.com/css2?family=Tinos:ital,wght@0,400;0,700;1,700&family=Open+Sans:wght@400&display=swap">
<style>
  :root {
    --navy: #124a78;
    --red: #e31b23;
    --white: #ffffff;
    --paper: #f5f5f5;
    --ink: #111111;
    --serif: "Tinos", "Times New Roman", serif;
    --sans: "Open Sans", Arial, sans-serif;
  }
  * { margin: 0; padding: 0; box-sizing: border-box; }
  html, body { width: 1200px; height: 1034px; overflow: hidden; background: var(--white); }
  .canvas { position: relative; width: 1200px; height: 1034px; font-family: var(--serif); color: var(--ink); }
  .abs { position: absolute; }

  /* cover page */
  .cover-photo { left: 0; top: 186px; width: 573px; height: 614px;
    background: radial-gradient(ellipse at 45% 55%, #d9d4cf 0%, #ece8e4 45%, #f6f4f2 100%); }
  .cover-shapes { left: 0; top: 0; }
  .issue-date, .issue-type { top: 14px; color: var(--white); font-size: 17px; }
  .issue-date { left: 12px; }
  .issue-type { left: 255px; }
  .cover-title { left: 0; top: 98px; width: 330px; text-align: center; color: var(--white);
    font-weight: 700; font-size: 27px; line-height: 35px; }
  .brand { left: 392px; top: 60px; width: 170px; text-align: center; }
  .brand-mark { color: var(--red); font-size: 62px; font-weight: 700; line-height: 64px; letter-spacing: 2px; }
  .brand-name { color: var(--navy); font-size: 8.6px; font-weight: 700; letter-spacing: .3px; margin-top: 2px; }

  .story-card { color: var(--white); text-align: center; font-size: 16px; line-height: 23px; }
  .story-card svg { position: absolute; left: 0; top: 0; }
  .story-card .card-text { position: relative; width: 177px; padding-top: 20px; }
  .story-card .card-line { display: block; white-space: nowrap; transform: scaleX(0.86); transform-origin: center; }
  .story-card h2 { font-size: 17px; font-weight: 700; line-height: 24px; }

  .cover-banner { left: 22px; top: 805px; width: 524px; height: 69px; }
  .cover-banner .band-red { position: absolute; left: 0; top: 0; width: 100%; height: 31px; background: var(--red); }
  .cover-banner .band-blue { position: absolute; left: 0; top: 31px; width: 100%; height: 38px; background: var(--navy); }
  .cover-banner p { position: relative; color: var(--white); font-style: italic; font-weight: 700;
    font-size: 12.2px; line-height: 17.5px; text-align: center; padding-top: 10px; white-space: nowrap; }
  .partner { left: 24px; top: 888px; display: flex; align-items: center; gap: 6px; }
  .partner-dot { width: 18px; height: 18px; border-radius: 50%; background: var(--navy); }
  .partner-name { color: var(--navy); font-size: 15px; font-weight: 700; }
  .partner-note { left: 134px; top: 888px; width: 420px; text-align: center; font-family: var(--sans);
    font-size: 14.5px; line-height: 19px; white-space: nowrap; }

  /* inside page */
  .inside-page { left: 618px; top: 4px; width: 576px; height: 991px; background: var(--paper); }
  .lead { left: 635px; top: 26px; width: 350px; text-align: center; font-family: var(--sans);
    color: var(--navy); font-size: 19px; line-height: 23.7px; }
  .pennant { left: 1014px; top: 4px; }
  .pennant-text { left: 1014px; top: 28px; width: 156px; text-align: center; color: var(--white);
    font-size: 21px; line-height: 27px; }
  .pennant-text h2 { font-size: 26px; font-weight: 700; line-height: 34px; margin-bottom: 6px; }

  .photo { background: linear-gradient(135deg, #5c4a3a 0%, #2f3f5a 45%, #6d6a63 100%); }
  .photo-one { left: 649px; top: 183px; width: 349px; height: 202px; }
  .photo-two { left: 898px; top: 569px; width: 279px; height: 197px;
    background: linear-gradient(135deg, #8a6a4a 0%, #3d5fb0 45%, #8b8066 100%); }
  .red-bar { background: var(--red); }
  .caption { background: var(--navy); color: var(--white); font-family: var(--sans); font-size: 14px;
    display: flex; align-items: center; justify-content: center; }
  .body-copy { font-size: 15.3px; line-height: 21px; }
  .related { left: 638px; top: 571px; width: 262px; text-align: center; color: var(--navy);
    font-size: 15.3px; line-height: 21px; }
  .body-large { font-size: 17px; line-height: 22.4px; }
  .page-tag { left: 1103px; top: 956px; width: 91px; height: 27px; }
  .page-tag .tag-line { height: 4px; background: var(--red); }
  .page-tag .tag-box { height: 23px; background: var(--navy); color: var(--white); font-weight: 700;
    font-size: 15.5px; text-align: center; line-height: 23px; }
</style>
</head>
<body>
<div class="canvas">

  <!-- Cover page -->
  <div class="abs cover-photo" role="img" aria-label="Soft-focus photo of a professional video camera"></div>

  <svg class="abs cover-shapes" width="576" height="300" viewBox="0 0 576 300">
    <polygon points="0,6 478,6 280,186 0,186" fill="var(--navy)"/>
    <path d="M190,275 C260,210 430,158 565,155 C580,160 575,175 560,185 C480,190 330,235 190,275 Z" fill="var(--navy)"/>
  </svg>

  <div class="abs issue-date">SPRING 2019</div>
  <div class="abs issue-type">SPECIAL EDITION</div>
  <h1 class="abs cover-title">POLICY AND PRIVACY<br>NEWSLETTER</h1>
  <div class="abs brand">
    <div class="brand-mark">PSTA</div>
    <div class="brand-name">PACIFIC SCREEN TRADE ALLIANCE</div>
  </div>

  <div class="abs story-card" style="left:17px;top:310px;width:195px;height:210px;">
    <svg width="195" height="210" viewBox="0 0 195 210">
      <polygon points="177,30 192,30 192,110 0,210 177,118" fill="var(--red)"/>
      <polygon points="0,0 177,0 177,122 0,208" fill="var(--navy)"/>
    </svg>
    <div class="card-text">
      <h2>SINGAPORE</h2>
      <span class="card-line">Ministry of Law announced</span>
      <span class="card-line">a policy change banning the</span>
      <span class="card-line">sale of ISDs and apps</span>
      <span class="card-line">PAGE 2</span>
    </div>
  </div>

  <div class="abs story-card" style="left:294px;top:311px;width:194px;height:210px;">
    <svg width="194" height="210" viewBox="0 0 194 210">
      <polygon points="178,30 192,30 192,108 0,210 178,118" fill="var(--red)"/>
      <polygon points="0,0 178,0 178,122 0,208" fill="var(--navy)"/>
    </svg>
    <div class="card-text" style="width:178px;padding-top:12px;">
      <h2>MALAYSIA</h2>
      <span class="card-line">Ministry of Law announced</span>
      <span class="card-line">a policy change banning the</span>
      <span class="card-line">sale of ISDs and apps</span>
      <span class="card-line">PAGE 3</span>
    </div>
  </div>

  <div class="abs story-card" style="left:73px;top:551px;width:194px;height:211px;">
    <svg width="194" height="211" viewBox="0 0 194 211">
      <polygon points="177,30 192,30 192,110 0,211 177,118" fill="var(--red)"/>
      <polygon points="0,0 177,0 177,122 0,209" fill="var(--navy)"/>
    </svg>
    <div class="card-text">
      <h2>PHILIPPINES</h2>
      <span class="card-line">New Online Infringement</span>
      <span class="card-line">Act backed by Meridian</span>
      <span class="card-line">Telecom and SRN</span>
      <span class="card-line">PAGE 3</span>
    </div>
  </div>

  <div class="abs story-card" style="left:351px;top:551px;width:193px;height:211px;">
    <svg width="193" height="211" viewBox="0 0 193 211">
      <polygon points="177,30 192,30 192,110 0,211 177,118" fill="var(--red)"/>
      <polygon points="0,0 177,0 177,122 0,209" fill="var(--navy)"/>
    </svg>
    <div class="card-text">
      <h2>THILAND</h2>
      <span class="card-line">Ministry of Law announced</span>
      <span class="card-line">a policy change banning the</span>
      <span class="card-line">sale of ISDs and apps</span>
      <span class="card-line">PAGE 4</span>
    </div>
  </div>

  <div class="abs cover-banner">
    <div class="band-red"></div>
    <div class="band-blue"></div>
    <p>The last few months have seen important antipiracy initiatives by several Asian governments.<br>For everyone’s convenience, we’ve brought together some short description in this<br>Special Edition of our Policy and Piracy Newsletter.</p>
  </div>

  <div class="abs partner">
    <span class="partner-dot"></span>
    <span class="partner-name">SRN</span>
  </div>
  <p class="abs partner-note">This Special Edition of the Policy and Piracy Newsletter<br>was created in collaboration with the<br>Screen Rights Network</p>

  <!-- Inside page -->
  <div class="abs inside-page"></div>

  <p class="abs lead">Main News - PSTA’s predecessor ABTC and other industry players had urged the Ministry in previous consultations to take action against ISDs, and this was a satisfying (if much-delayed) response.</p>

  <svg class="abs pennant" width="182" height="326" viewBox="0 0 182 326">
    <polygon points="19,0 182,0 182,156 19,322" fill="var(--red)"/>
    <polygon points="0,2 155,2 155,180 0,314" fill="var(--navy)"/>
  </svg>
  <div class="abs pennant-text">
    <h2>SINGAPORE</h2>
    New laws to be tabled soon to ban sale of illegal streaming devices in Singapore
  </div>

  <div class="abs photo photo-one" role="img" aria-label="Electronics shop with streaming boxes and TV screens on display"></div>
  <div class="abs red-bar" style="left:998px;top:364px;width:171px;height:21px;"></div>
  <div class="abs caption" style="left:743px;top:385px;width:426px;height:30px;">DESCRIPTION OF THE IMAGE &amp; ITS REFERENCE</div>

  <p class="abs body-copy" style="left:665px;top:430px;width:522px;">Detail of Main News SINGAPORE - New laws will be tabled in Parliament some time this year to ban the sale of media streaming boxes with "add-on" services that help consumers access pirated content.This clarity comes on the heels of a three-year review by the Ministry of Law (MinLaw) and the Intellectual Property Office of Singapore (Ipos) of copyright laws here.</p>

  <p class="abs related">Other related News The second notable Singapore injunction came in respect to a block order issued against streaming websites – allowing content owners and ISPs to work together to make the blocks “dynamic” and follow the pirate sites when they change domains.</p>

  <div class="abs photo photo-two" role="img" aria-label="Shop display of a streaming box menu on a screen with price stickers"></div>
  <div class="abs red-bar" style="left:711px;top:748px;width:187px;height:18px;"></div>
  <div class="abs caption" style="left:711px;top:766px;width:401px;height:30px;">DESCRIPTION OF THE IMAGE &amp; ITS REFERENCE</div>

  <p class="abs body-large" style="left:655px;top:821px;width:524px;">Details of the second news - New laws will be tabled in Parliament some time this year to ban the sale of media streaming boxes with "add-on" services that help consumers access pirated content.This clarity comes on the heels of a three-year review by the Ministry of Law (MinLaw) and the Intellectual Property Office of Singapore (Ipos) of copyright laws here.</p>

  <div class="abs page-tag">
    <div class="tag-line"></div>
    <div class="tag-box">Page 2</div>
  </div>

</div>
</body>
</html>
```